P.K.Harbor Services Business Card

We need a bi-lingual card (spanish/english). Information should be name, hours, services and address/phone. I am including a flyer as a reference--much of the information is included on it (spanish/english as well). THE COMPANY IS CALLED "P.K. HARBOR SERVICES" AND WE THINK THAT "P.K." SHOULD SUFFICE AS A LOGO--BUT WE DON'T HAVE THAT FONT NAILED DOWN. Colors should be Green/Blue scale. Happy colors. It's a check cashing business.

```html
<!DOCTYPE html>
<html lang="en">
<head>
<meta charset="utf-8">
<title>P.K. Harbor Services – Business Card</title>
<link href="https://fonts.googleapis.com/css2?family=Paytone+One&family=Rubik:wght@800;900&family=Montserrat:wght@500;600&display=swap" rel="stylesheet">
<style>
  :root {
    --stage: #a6a6a6;
    --paper: #ffffff;
    --navy: #233b8e;
    --navy-deep: #1f3784;
    --sky: #2bb5fb;
    --red: #e01b0c;
    --yellow: #fff200;
    --band: #e7ebf7;
  }
  * { margin: 0; padding: 0; box-sizing: border-box; }
  html, body { width: 1200px; height: 447px; overflow: hidden; background: var(--stage); }
  .canvas { position: relative; width: 1200px; height: 447px; }

  .card { position: absolute; background: var(--paper); overflow: hidden; }
  .card-front { left: 113px; top: 84px; width: 429px; height: 246px; }
  .card-back  { left: 639px; top: 82px; width: 429px; height: 245px; }

  .corner { position: absolute; inset: 0; width: 100%; height: 100%; }

  .brand {
    font-family: "Paytone One", sans-serif;
    color: var(--navy);
    white-space: nowrap;
    text-align: center;
    position: absolute; left: 0; right: 0;
  }
  .card-front .brand { top: 97px; font-size: 35px; line-height: 40px; letter-spacing: 0.2px; }
  .card-back .brand  { top: 15px; font-size: 28px; line-height: 34px; }

  .service {
    position: absolute; left: 0; right: 0; top: 62px;
    text-align: center;
    font-family: "Rubik", sans-serif; font-weight: 900;
    font-size: 27px; line-height: 32px;
    color: var(--red);
  }
  .tagline {
    position: absolute; left: 0; right: 0; top: 94px;
    text-align: center;
    font-family: "Rubik", sans-serif; font-weight: 800;
    font-size: 12.5px; line-height: 16px;
    color: var(--navy);
  }
  .language-pill {
    position: absolute; left: 153px; top: 117px; width: 131px; height: 20px;
    border-radius: 10px; background: var(--yellow);
    font-family: "Rubik", sans-serif; font-weight: 800;
    font-size: 10px; line-height: 20px; text-align: center;
    color: var(--red);
  }

  .divider { position: absolute; top: 167px; height: 2px; }
  .divider-red { left: 0; width: 211px; background: var(--red); }
  .divider-blue { left: 214px; right: 0; background: var(--navy); }

  .contact-band { position: absolute; left: 0; right: 0; top: 169px; bottom: 0; background: var(--band); }

  .contact-icon { position: absolute; width: 21px; height: 21px; }
  .contact-text {
    position: absolute;
    font-family: "Montserrat", sans-serif; font-weight: 500;
    color: var(--navy); white-space: nowrap;
  }
  .address { left: 61px; top: 187px; font-size: 8.3px; }
  .phone   { left: 60px; top: 216px; font-size: 8.3px; }
  .hours   { left: 285px; top: 185px; font-size: 7.2px; line-height: 13.5px; }
</style>
</head>
<body>
<div class="canvas">

  <section class="card card-front">
    <svg class="corner" viewBox="0 0 429 246" aria-hidden="true">
      <polygon points="0,0 36,0 0,82" fill="var(--sky)"/>
      <polygon points="429,162 429,246 396,246" fill="var(--navy-deep)"/>
    </svg>
    <h1 class="brand">P.K. HARBOR SERVICES</h1>
  </section>

  <section class="card card-back">
    <h2 class="brand">P.K. HARBOR SERVICES</h2>
    <p class="service">CHECK CA$HING</p>
    <p class="tagline">ALL CHECKS WELCOME! BEST RATES IN WESTCHESTER</p>
    <p class="language-pill">¡SE HABLA ESPAÑOL!</p>

    <div class="divider divider-red"></div>
    <div class="divider divider-blue"></div>
    <div class="contact-band"></div>

    <svg class="contact-icon" style="left:31px;top:182px" viewBox="0 0 20 20" aria-hidden="true">
      <circle cx="10" cy="10" r="10" fill="var(--navy)"/>
      <path d="M10 4.5a3.4 3.4 0 0 0-3.4 3.4c0 2.5 3.4 6.4 3.4 6.4s3.4-3.9 3.4-6.4A3.4 3.4 0 0 0 10 4.5z" fill="#fff"/>
      <circle cx="10" cy="7.9" r="1.2" fill="var(--navy)"/>
    </svg>
    <p class="contact-text address">48 ORCHARD LANE MILLBROOK, NY</p>

    <svg class="contact-icon" style="left:32px;top:211px" viewBox="0 0 20 20" aria-hidden="true">
      <circle cx="10" cy="10" r="10" fill="var(--navy)"/>
      <path d="M6.6 5.2l1.6-.4 1.1 2.6-1 .9a6.5 6.5 0 0 0 3 3l.9-1 2.6 1.1-.4 1.6c-.2.6-.8.9-1.4.8-3.8-.6-6.6-3.4-7.2-7.2-.1-.6.2-1.2.8-1.4z" fill="#fff"/>
    </svg>
    <p class="contact-text phone">(555) 204 - 3170</p>

    <svg class="contact-icon" style="left:258px;top:184px" viewBox="0 0 20 20" aria-hidden="true">
      <circle cx="10" cy="10" r="10" fill="var(--navy)"/>
      <circle cx="10" cy="10" r="4.6" fill="none" stroke="#fff" stroke-width="1.4"/>
      <path d="M10 7.4V10H8.2" fill="none" stroke="#fff" stroke-width="1.3" stroke-linecap="round"/>
    </svg>
    <p class="contact-text hours">ONDAY-SATURDAY, 9AM-9PM<br>MONDAY-SATURDAY, 9AM-9PM</p>
  </section>

</div>
</body>
</html>
```